Carpet cleaning company wants business card

Need an exciting new fresh design for business cards for my carpet cleaning /pest control business
www.tidewellhomecare.com.au
Can design include a lined section for quoting or information? Thanks !

```html
<!DOCTYPE html>
<html lang="en">
<head>
<meta charset="utf-8">
<title>Tidewell Home Care – Business Card</title>
<link rel="stylesheet" href="https://fonts.googleapis.com/css2?family=Arimo:wght@400;700&display=swap">
<style>
  :root {
    --stage: #3b3b3b;
    --card: #ffffff;
    --brand-red: #e4343c;
    --brand-blue: #0a4f9c;
    --rule-blue: #2f6fb7;
  }
  * { box-sizing: border-box; margin: 0; padding: 0; }
  html, body {
    width: 1200px;
    height: 900px;
    overflow: hidden;
    background: var(--stage);
    font-family: "Arimo", Arial, sans-serif;
  }
  .card {
    position: absolute;
    top: 302px;
    width: 513px;
    height: 295px;
    background: var(--card);
    border-radius: 22px;
    box-shadow: 0 4px 12px rgba(0,0,0,0.35);
  }
  .card--back { left: 72px; }
  .card--front { left: 615px; text-align: center; }

  .brand {
    display: flex;
    align-items: center;
    justify-content: center;
    gap: 10px;
    font-weight: 700;
    color: var(--brand-blue);
    letter-spacing: -0.5px;
    white-space: nowrap;
  }
  .brand__mark {
    display: block;
    background: var(--brand-red);
  }
  .card--back .brand {
    position: absolute;
    top: 32px;
    left: 0;
    right: 0;
    font-size: 32px;
  }
  .card--back .brand__mark { width: 22px; height: 22px; }

  .quote-lines {
    position: absolute;
    left: 39px;
    right: 39px;
    top: 149px;
    list-style: none;
  }
  .quote-lines li {
    height: 1px;
    background: var(--rule-blue);
    margin-bottom: 38px;
  }

  .person__name {
    margin-top: 22px;
    font-size: 35px;
    font-weight: 700;
    color: var(--brand-red);
    line-height: 1.1;
  }
  .person__role {
    font-size: 13px;
    font-weight: 700;
    color: var(--brand-blue);
    margin-top: 2px;
  }
  .card--front .brand {
    margin-top: 34px;
    font-size: 40px;
  }
  .card--front .brand__mark { width: 28px; height: 28px; }
  .contact__phone {
    margin-top: 36px;
    font-size: 38px;
    font-weight: 700;
    color: var(--brand-red);
    letter-spacing: 0.5px;
    line-height: 1;
  }
  .contact__web {
    margin-top: 4px;
    font-size: 13px;
    font-weight: 700;
    color: var(--brand-blue);
  }
</style>
</head>
<body>
  <section class="card card--back" aria-label="Card back with quote lines">
    <div class="brand"><span class="brand__mark"></span>Tidewell Home Care</div>
    <ul class="quote-lines">
      <li></li><li></li><li></li><li></li>
    </ul>
  </section>

  <section class="card card--front" aria-label="Card front">
    <h1 class="person__name">Daniel Hartley</h1>
    <p class="person__role">managing director</p>
    <div class="brand"><span class="brand__mark"></span>Tidewell Home Care</div>
    <p class="contact__phone">555 0142 7788</p>
    <p class="contact__web">www.tidewellhomecare.com.au</p>
  </section>
</body>
</html>
```